依頼詳細
種の袋を陳列棚に並べて販売しております。他社の種の販売もされている中で自社の種の袋が目立ち最新のデザインでお客様の目を引くようなものをデザインしていただければと思います。
記載項目
サイズ:W9.8mm×H15.6mm 印刷/両面カラー
希望イメージ
シンプル 複雑
単色 カラフル
暗い 明るい
日常 高級
遊び心 厳粛
未来的 伝統的
女性的 男性的
希望する色
赤系、黄・オレンジ系
納品ファイル
• イラストレーター形式 (.ai)
• フォトショップ形式 (.psd)
補足説明
パワーポイントデータにデザイン指示書があります。
現在のパッケージも添付します。
陳列棚のイメージも添付します。
ハヤセミドリにもデザインが並ぶかもしれませんので素晴らしいデザインをお願いします。
依頼公開後の追記内容
北浜青果園ホームページ

http://www.kitahama-seika.example.jp/
表面の商品名(ほうれん草)は、上から4.5センチ以内にデザインをお願いします。
(陳列棚に並べたときに見えるように)

料金の表示枠もデザインに入れてください。
左から1センチ上から5.9センチのところから白枠を付けてください。
白枠はW1.7×1センチ 角丸

詳細が遅くなりすみません。よろしくお願いします。
■ 選んだ理由

今までの概念にないデザインをしていただきありがとうございました。某有名ドラックストアにてこのデザインの種を販売する予定です。楽しみにお待ちください。お客様がとても喜んでおりました。今後他の種類の野菜もデザインを増やしていく予定ですのでその際は宜しくお願いします。

■ 提案者全員のお礼・コメント

複数のデザインありがとうございました。今後もコンペを行っていきますのでよろしくお願いします。

```html
<!DOCTYPE html>
<html lang="ja">
<head>
<meta charset="utf-8">
<title>やさいのたね ほうれん草</title>
<link rel="stylesheet" href="https://fonts.googleapis.com/css2?family=M+PLUS+Rounded+1c:wght@500;800&display=swap">
<style>
:root{
  --orange:#ee6a12;
  --orange-deep:#d9510a;
  --yellow:#ffe33a;
  --green:#2f9a3a;
  --green-deep:#1f7a2a;
  --white:#ffffff;
  --ink:#3a2a1a;
  --table-bg:rgba(255,255,255,.88);
  --bar:#f08a24;
}
*{margin:0;padding:0;box-sizing:border-box}
html,body{width:761px;height:1200px;overflow:hidden;background:#fff}
body{font-family:"M PLUS Rounded 1c",sans-serif}
.packet{position:relative;width:761px;height:1200px;overflow:hidden}
.backdrop-photo{position:absolute;inset:0;
  background:linear-gradient(160deg,#7c9a3a 0%,#c7452d 22%,#6d8a2e 45%,#3f6b26 70%,#b4432a 100%)}
.produce-photo{position:absolute;left:120px;top:250px;width:620px;height:500px;border-radius:50%;
  background:radial-gradient(ellipse at 50% 50%,#2f5d22 0%,#3c7a2b 45%,#e9eee6 68%,#f6f6f4 80%,rgba(246,246,244,0) 100%)}
.header{position:absolute;left:50px;top:64px;width:660px;height:180px;background:var(--orange);
  border-radius:22px;box-shadow:0 6px 0 var(--orange-deep)}
.series-tag{position:absolute;left:228px;top:10px;width:305px;height:68px;background:var(--yellow);
  border-radius:34px;border:5px solid var(--orange);display:flex;align-items:center;justify-content:center;
  font-weight:800;font-size:33px;color:var(--orange-deep);gap:8px;white-space:nowrap}
.series-tag svg{width:36px;height:32px;flex:none}
.product-name{position:absolute;left:50px;top:100px;width:660px;text-align:center;
  font-weight:800;font-size:118px;line-height:1;color:var(--white);letter-spacing:2px;
  text-shadow:0 4px 0 var(--orange-deep)}
.price-box{position:absolute;left:89px;top:440px;width:132px;height:80px;background:var(--white);
  border-radius:14px;border:3px solid #ddd;padding:8px 12px;color:var(--ink)}
.price-box .tax{font-size:18px;font-weight:500;line-height:1.2}
.price-box .amount{font-size:30px;font-weight:800;text-align:right;line-height:1.3;white-space:nowrap}
.ribbon{position:absolute;left:238px;top:600px;width:500px;height:88px;background:var(--green);
  transform:rotate(-3deg);display:flex;align-items:center;justify-content:center;
  font-weight:800;font-size:44px;color:var(--yellow);border:4px solid var(--white);
  box-shadow:0 5px 10px rgba(0,0,0,.3);white-space:nowrap}
.germ-info{position:absolute;left:18px;top:742px;color:var(--white);font-weight:800;font-size:27px;line-height:1.45;
  text-shadow:0 0 4px rgba(0,0,0,.7);white-space:nowrap}
.germ-info span{display:inline-block;width:210px}
.calendar{position:absolute;left:14px;top:836px;width:480px;background:var(--table-bg);border-radius:6px;padding:6px;
  display:grid;grid-template-columns:84px repeat(12,1fr);grid-auto-rows:42px;font-weight:800;font-size:19px;color:var(--ink)}
.calendar .cell{display:flex;align-items:center;justify-content:center;border-right:1px solid #c8c8c8;border-bottom:1px solid #c8c8c8;position:relative}
.calendar .head{background:var(--yellow)}
.calendar .label{background:#fff3c4}
.bar{position:absolute;top:14px;height:14px;background:var(--bar);border-radius:3px}
.icon-illustration{position:absolute;left:505px;top:1020px;width:240px;height:100px;border-radius:10px;
  background:linear-gradient(180deg,#5fa64a,#8a5a34)}
.maker-band{position:absolute;left:0;top:1117px;width:761px;height:83px;background:var(--white);
  display:flex;align-items:center;padding-left:26px;gap:14px;color:var(--green-deep);font-weight:800}
.maker-band .mark{width:44px;height:44px;border-radius:50%;background:var(--green-deep)}
.maker-band .corp{font-size:16px}
.maker-band .name{font-size:34px}
</style>
</head>
<body>
<div class="packet">
  <div class="backdrop-photo" role="img" aria-label="色とりどりの野菜を並べた写真"></div>
  <div class="produce-photo" role="img" aria-label="白い皿に盛られたほうれん草の写真"></div>

  <div class="header"></div>
  <div class="series-tag">やさいのたね
    <svg viewBox="0 0 38 34"><path d="M19 34V16" stroke="#2f9a3a" stroke-width="4" fill="none"/><path d="M19 18C10 18 4 12 3 4c9 0 15 5 16 14z" fill="#2f9a3a"/><path d="M19 16c2-8 8-13 16-13-1 8-7 13-16 13z" fill="#4bb548"/></svg>
  </div>
  <h1 class="product-name">ほうれん草</h1>

  <div class="price-box"><div class="tax">税込</div><div class="amount">210円</div></div>

  <div class="ribbon">プランターでも栽培可能</div>

  <p class="germ-info"><span>発芽適温(地温)</span>15℃~20℃<br><span>発芽日数</span>適温(地温)で約3~6日位</p>

  <div class="calendar">
    <div class="cell head">栽培例</div>
    <div class="cell head">1</div><div class="cell head">2</div><div class="cell head">3</div><div class="cell head">4</div><div class="cell head">5</div><div class="cell head">6</div><div class="cell head">7</div><div class="cell head">8</div><div class="cell head">9</div><div class="cell head">10</div><div class="cell head">11</div><div class="cell head">12</div>
    <div class="cell label">冷涼地</div>
    <div class="cell"></div><div class="cell"></div><div class="cell"><i class="bar" style="left:0;width:100%"></i></div><div class="cell"><i class="bar" style="left:0;width:100%"></i></div><div class="cell"><i class="bar" style="left:0;width:100%"></i></div><div class="cell"><i class="bar" style="left:0;width:100%"></i></div><div class="cell"><i class="bar" style="left:0;width:100%"></i></div><div class="cell"><i class="bar" style="left:0;width:100%"></i></div><div class="cell"><i class="bar" style="left:0;width:60%"></i></div><div class="cell"></div><div class="cell"></div><div class="cell"></div>
    <div class="cell label">中間地</div>
    <div class="cell"></div><div class="cell"></div><div class="cell"><i class="bar" style="left:40%;width:60%"></i></div><div class="cell"><i class="bar" style="left:0;width:100%"></i></div><div class="cell"><i class="bar" style="left:0;width:50%"></i></div><div class="cell"></div><div class="cell"></div><div class="cell"></div><div class="cell"><i class="bar" style="left:0;width:100%"></i></div><div class="cell"><i class="bar" style="left:0;width:100%"></i></div><div class="cell"><i class="bar" style="left:0;width:50%"></i></div><div class="cell"></div>
    <div class="cell label">暖地</div>
    <div class="cell"></div><div class="cell"></div><div class="cell"><i class="bar" style="left:0;width:100%"></i></div><div class="cell"><i class="bar" style="left:0;width:50%"></i></div><div class="cell"></div><div class="cell"></div><div class="cell"></div><div class="cell"></div><div class="cell"><i class="bar" style="left:40%;width:60%"></i></div><div class="cell"><i class="bar" style="left:0;width:100%"></i></div><div class="cell"><i class="bar" style="left:0;width:100%"></i></div><div class="cell"></div>
  </div>

  <div class="icon-illustration" role="img" aria-label="土から育つほうれん草のイラスト"></div>

  <footer class="maker-band">
    <span class="mark"></span>
    <span class="corp">株式会社</span>
    <span class="name">北浜青果園</span>
  </footer>
</div>
</body>
</html>
```